Corporate Wall Mural for Office

We have several offices across North America and we want to have a corporate wall mural in each office, so we require a mural wall design that can be adjusted for different wall dimensions and still look good.

The first mural will be 239.5" x 112.5" it will be in our Toronto office - so the background city will be the Toronto skyline

I have attached a draft design and the content PNG file.

We want a different design that keeps the content outlined in the Mural Design Content PNG file.

Our corporate font is Gilroy Semi Bold

Our corporate colors are
Blue
C94
M70
Y0
K12
Pantone 2945C

Purple
C 80
M 78
PMS 2368 C

Sky Blue
C68
M34
PMS 2727 C
Our website is qalverpoint.com

Founded in 2012, QPT is a leading provider of technology infrastructure solutions, specializing in Broadband, DAS/Private Networks, Fixed Wireless Access, Site Solutions, Carrier Networks, and Test & Measurement. Our mission is to empower organizations of all sizes with innovative connectivity and telecom infrastructure solutions to build the future of communications.

Target Market(s)

Target is the staff and visitors of our office

Industry/Entity Type

network infrastructure: both wireless and wireline

Font styles to use
Sans Serif
Other font styles liked:
• Gilroy Semi-Bold and Bold

Colors
0054AA
0677BA
7BADD7
CADEEF
E8F1F8

Requirements
Must have
• the info listed in the Mural Content.png file, our corporate colors. It should be bright and energetic.
Nice to have
• I like concept of the city silhouette from the draft design

```html
<!DOCTYPE html>
<html lang="en">
<head>
<meta charset="utf-8">
<title>QPT Office Mural</title>
<link href="https://fonts.googleapis.com/css2?family=Barlow+Condensed:wght@600;700&family=Montserrat:wght@400;500;700;800&display=swap" rel="stylesheet">
<style>
  :root {
    --purple: #5452a3;
    --purple-deep: #3e3e96;
    --blue: #2f80dc;
    --blue-dark: #134f99;
    --blue-mid: #2855b8;
    --sky: #7badd7;
    --white: #ffffff;
    --ink: #111111;
    --value-text: #1f5bbf;
    --lavender: #d9d8ec;
  }
  html, body { margin: 0; padding: 0; overflow: hidden; }
  body { background: var(--purple); }
  .mural {
    position: relative; width: 1200px; height: 564px; overflow: hidden;
    background: var(--purple); font-family: "Montserrat", sans-serif;
  }
  .mural-shapes { position: absolute; inset: 0; }
  .condensed { font-family: "Barlow Condensed", sans-serif; font-weight: 700; }
  .abs { position: absolute; margin: 0; }

  .brand-name { left: 140px; top: 38px; font-size: 54px; font-weight: 800; color: var(--ink); letter-spacing: 1px; line-height: 1; }
  .brand-url { left: 143px; top: 90px; font-size: 14px; font-weight: 500; color: var(--ink); }

  .unique-title { left: 42px; top: 128px; font-size: 29px; color: var(--white); }

  .trait { position: absolute; left: 6px; display: flex; align-items: center; }
  .trait-label { width: 136px; text-align: right; color: var(--white); font-weight: 800; font-size: 11.5px; line-height: 1.2; }
  .trait-value { position: absolute; left: 146px; color: var(--value-text); font-weight: 500; font-size: 11px; line-height: 1.25; white-space: nowrap; }

  .values-title { left: 31px; top: 307px; font-size: 24px; color: var(--purple-deep); letter-spacing: .3px; }
  .values-list { left: 27px; top: 342px; list-style: none; padding: 0; }
  .values-list li { height: 21.6px; line-height: 21px; color: var(--white); font-size: 13.5px; }

  .bullet::before { content: ""; display: inline-block; width: 6px; height: 6px; background: var(--white); margin-right: 7px; vertical-align: 2px; }

  .headline { left: 480px; top: 38px; width: 660px; text-align: center; font-size: 33px; color: var(--white); letter-spacing: .4px; line-height: 1.1; }
  .subline { left: 480px; top: 76px; width: 680px; text-align: center; font-size: 19px; font-weight: 600; color: var(--purple-deep); font-family: "Barlow Condensed", sans-serif; }

  .pill-label { top: 119px; font-size: 20px; color: var(--white); text-align: center; }

  .list { list-style: none; padding: 0; top: 166px; }
  .list li { height: 21.6px; line-height: 21px; color: var(--white); font-size: 14px; white-space: nowrap; }
  .list li.two-line { white-space: normal; line-height: 16px; height: auto; padding-top: 3px; }
  .list li.two-line span { display: block; padding-left: 13px; }
</style>
</head>
<body>
<main class="mural">
  <svg class="mural-shapes" width="1200" height="564" viewBox="0 0 1200 564" aria-hidden="false">
    <defs>
      <linearGradient id="headerBand" x1="0" x2="1" y1="0" y2="0">
        <stop offset="0" stop-color="#2f6fd0"/><stop offset=".5" stop-color="#1f4fae"/><stop offset="1" stop-color="#2f80dc"/>
      </linearGradient>
      <linearGradient id="listBox" x1="0" x2="0" y1="0" y2="1">
        <stop offset="0" stop-color="#5050a2"/><stop offset="1" stop-color="#2f80dc"/>
      </linearGradient>
      <linearGradient id="skylineTone" x1="0" x2="0" y1="0" y2="1">
        <stop offset="0" stop-color="#e4e3f2"/><stop offset=".55" stop-color="#a9a7d4"/><stop offset="1" stop-color="#5a55a8"/>
      </linearGradient>
    </defs>
    <!-- central white field -->
    <polygon points="448,6 1165,6 950,558 265,558" fill="var(--white)"/>
    <!-- left blue field -->
    <polygon points="6,6 448,6 265,558 6,558" fill="var(--blue)"/>
    <!-- skyline area -->
    <g role="img" aria-label="City skyline silhouette with a tall communications tower">
      <polygon points="268,330 1000,330 1000,558 268,558" fill="url(#skylineTone)"/>
      <polygon points="70,465 270,465 270,558 70,558" fill="#2360d6"/>
    </g>
    <!-- logo card -->
    <polygon points="6,30 400,30 368,115 6,115" fill="var(--white)"/>
    <polygon points="400,22 455,22 418,122 365,122" fill="var(--purple)"/>
    <circle cx="80" cy="72" r="28" fill="var(--blue-dark)"/>
    <!-- unique table -->
    <rect x="6" y="168" width="364" height="120" fill="var(--purple)"/>
    <polygon points="145,171 369,171 362,191 145,191" fill="var(--white)"/>
    <polygon points="145,198 360,198 352,229 145,229" fill="var(--white)"/>
    <polygon points="145,236 348,236 342,256 145,256" fill="var(--white)"/>
    <polygon points="145,263 338,263 331,284 145,284" fill="var(--white)"/>
    <rect x="6" y="192" width="360" height="5" fill="var(--blue)"/>
    <rect x="6" y="230" width="350" height="5" fill="var(--blue)"/>
    <rect x="6" y="257" width="340" height="5" fill="var(--blue)"/>
    <!-- core values -->
    <polygon points="6,308 232,308 248,337 6,337" fill="var(--white)"/>
    <polygon points="6,342 248,342 241,360 6,360" fill="var(--blue-dark)"/>
    <polygon points="6,364 240,364 233,382 6,382" fill="var(--blue-dark)"/>
    <polygon points="6,386 232,386 225,404 6,404" fill="var(--blue-dark)"/>
    <polygon points="6,407 224,407 217,425 6,425" fill="var(--blue-dark)"/>
    <polygon points="6,429 216,429 209,447 6,447" fill="var(--blue-dark)"/>
    <!-- headline band -->
    <polygon points="490,37 1145,37 1130,76 475,76" fill="url(#headerBand)"/>
    <!-- pills -->
    <rect x="440" y="117" width="172" height="31" rx="15.5" fill="var(--blue-mid)"/>
    <rect x="642" y="117" width="186" height="31" rx="15.5" fill="var(--blue-mid)"/>
    <rect x="883" y="117" width="158" height="31" rx="15.5" fill="var(--blue-mid)"/>
    <!-- list boxes -->
    <polygon points="408,156 612,156 612,325 345,325" fill="url(#listBox)"/>
    <rect x="649" y="156" width="165" height="169" fill="url(#listBox)"/>
    <polygon points="841,156 1098,156 1038,325 841,325" fill="url(#listBox)"/>
  </svg>

  <p class="abs brand-name">QPT</p>
  <p class="abs brand-url">www.qalverpoint.com</p>

  <h2 class="abs condensed unique-title">What Makes Us Unique?</h2>

  <div class="trait" style="top:171px;height:20px"><span class="trait-label">QPT TOUCH:</span><span class="trait-value">We are more than a catalog</span></div>
  <div class="trait" style="top:198px;height:31px"><span class="trait-label">QPT EXPERIENCE:</span><span class="trait-value">A pleasure to do business with<br>Proactive, Professional and Precise</span></div>
  <div class="trait" style="top:236px;height:20px"><span class="trait-label">QPT SOLUTION:</span><span class="trait-value">Design, Develop, and Deliver</span></div>
  <div class="trait" style="top:263px;height:21px"><span class="trait-label">CUSTOM SOLUTIONS:</span><span class="trait-value">On-Time and On-Spec</span></div>

  <h2 class="abs condensed values-title">OUR CORE VALUES</h2>
  <ul class="abs values-list">
    <li class="bullet">People First</li>
    <li class="bullet">Customer Focus</li>
    <li class="bullet">Work Smart</li>
    <li class="bullet">Customer Improvement</li>
    <li class="bullet">Results Matter</li>
  </ul>

  <h1 class="abs condensed headline">ENABLING SOLUTIONS FOR A CONNECTED WORLD</h1>
  <p class="abs subline">WE DISTRIBUTE PRODUCTS AND SOLUTION SERVICES FOR DIGITAL INFRASTRUCTURE</p>

  <h3 class="abs condensed pill-label" style="left:440px;width:172px">OUR CAPABILITIES</h3>
  <h3 class="abs condensed pill-label" style="left:642px;width:186px">SOLUTION SERVICES</h3>
  <h3 class="abs condensed pill-label" style="left:883px;width:158px">OUR MARKETS</h3>

  <ul class="abs list" style="left:418px">
    <li class="bullet">Wireless Infrastructure</li>
    <li class="bullet">Broadband &amp; Fiber</li>
    <li class="bullet">Site Solutions</li>
    <li class="bullet">Fixed Wireless Acess</li>
    <li class="bullet">Test Measurement</li>
    <li class="bullet">DAS&amp; PWN</li>
    <li class="bullet">Power Solutions</li>
  </ul>
  <ul class="abs list" style="left:664px">
    <li class="bullet">Kitting &amp; Logistics</li>
    <li class="bullet">Professional</li>
    <li class="bullet">Engineering</li>
    <li class="bullet">Place Holder</li>
    <li class="bullet">Place Holder</li>
    <li class="bullet">Place Holder</li>
  </ul>
  <ul class="abs list" style="left:854px">
    <li class="bullet">Carriers &amp; Cable Companies</li>
    <li class="bullet">Data Centers</li>
    <li class="bullet">Utilities</li>
    <li class="bullet">Federal Government</li>
    <li class="bullet">Education</li>
    <li class="bullet two-line">Industrial Manufacturing<span>&amp; Digital Supply Chain</span></li>
  </ul>
</main>
</body>
</html>
```